Small Salsa business needs web design + coding

LA Brisa Roja is a small business started in Pocatello, Idaho and is looking to expand online. We focus on keeping the salsa all natural and more about savor than spiciness. Similar to the photo we've attached of just one of our salsas, we want a website that is friendly for users of all ages to use, as well as advertising in the website, and offer online shopping. Other things you think is beneficial to a small business like ours, proposals are welcomed and encouraged. We would also like to be able to remove and add stuff as we continue to grow our business.

```html
<!DOCTYPE html>
<html lang="en">
<head>
<meta charset="utf-8">
<title>LA Brisa Roja — Salsa</title>
<link rel="stylesheet" href="https://fonts.googleapis.com/css2?family=Bree+Serif&family=Archivo+Narrow:wght@400;600;700&display=swap">
<style>
:root{
  --orange:#dd6413;
  --orange-soft:rgba(221,100,19,.82);
  --stage:#6e6e6e;
  --ink:#1b1b1b;
  --body:#3a3a3a;
  --white:#ffffff;
  --footer:#2a231e;
  --line:#d6d6d6;
}
*{margin:0;padding:0;box-sizing:border-box}
html,body{width:1028px;height:1200px;overflow:hidden}
body{background:var(--stage);position:relative;font-family:"Archivo Narrow",sans-serif;color:var(--body)}
.page{position:absolute;background:var(--white);overflow:hidden}
.page *{position:absolute}
.page-home{left:9px;top:11px;width:498px;height:1147px}
.page-app{left:520px;top:11px;width:498px;height:1178px}
.serif{font-family:"Bree Serif",serif}
.photo{display:block}
.center{text-align:center}
.nav a,.nav span{color:var(--white);font-size:6px;font-weight:700;text-decoration:none;letter-spacing:.1px}
.btn{background:var(--orange);color:var(--white);border-radius:9px;font-family:"Bree Serif",serif;font-size:6px;display:flex;align-items:center;justify-content:center;letter-spacing:.2px}
.btn-light{background:var(--white);color:var(--orange)}

/* home page */
.topbar{left:0;top:0;width:498px;height:14px;background:var(--orange)}
.topbar span{top:4px;font-size:4.6px;color:var(--white);font-weight:600}
.dot{width:4px;height:4px;border-radius:50%;background:var(--white)}
.hero{left:0;top:14px;width:498px;height:231px;background:radial-gradient(ellipse at 65% 45%,#8a2c1c 0%,#5a2616 45%,#2a1a12 100%)}
.brand-light{font-family:"Bree Serif",serif;color:var(--white);font-size:15px;line-height:1}
.brand-dark{font-family:"Bree Serif",serif;color:var(--ink);font-size:15px;line-height:1}
.brand-mark{width:7px;height:7px;background:var(--orange)}
.offer{border-radius:50%;display:block}
.offer-title{font-family:"Bree Serif",serif;color:var(--white);font-size:24px;line-height:1;width:100%;text-align:center}
.offer-text{color:var(--white);font-size:5.6px;line-height:12.5px;width:100%;text-align:center}
.offer-pct{font-family:"Archivo Narrow",sans-serif;font-weight:700;color:var(--white);font-size:24px;line-height:1;width:100%;text-align:center}
.section-title{font-family:"Bree Serif",serif;color:var(--ink);font-size:14px;line-height:1;white-space:nowrap}
.tile{width:97px;height:98px}
.tile-price{top:5px;right:6px;background:var(--orange);color:var(--white);font-size:5.2px;font-weight:700;padding:1px 5px;border-radius:5px;position:absolute}
.tile-name{bottom:12px;left:0;width:100%;text-align:center;color:var(--white);font-size:8.5px;font-weight:600;position:absolute}
.para{font-size:5.6px;line-height:12.5px;color:var(--body)}
.ingredients li{list-style:none;font-size:5.8px;font-weight:700;color:var(--ink);padding-left:9px;line-height:7px;width:64px}
.ingredients li::before{content:"";position:absolute;left:0;top:1px;width:5px;height:5px;border-radius:50%;background:var(--orange)}
.ingredients li.two-line{line-height:12px}
.ingredients li.two-line::before{top:3px}
.footer{left:0;top:1014px;width:498px;height:133px;background:linear-gradient(180deg,#3a2a1f,#201a16)}
.footer-text{color:var(--white);font-size:6px;line-height:12px}
.footer-nav span{color:var(--white);font-size:6px;font-weight:700;width:80px;text-align:center;left:0}

/* app page */
.nav-dark span{color:var(--ink);font-size:6px;font-weight:700}
.search{left:46px;top:161px;width:165px;height:22px;border-radius:11px;background:var(--white);box-shadow:0 1px 4px rgba(0,0,0,.18)}
.store{width:76px;height:23px;border-radius:4px;background:#111}
.card{width:92px;height:110px;background:var(--white);border-radius:7px;box-shadow:0 1px 6px rgba(0,0,0,.14);overflow:hidden}
.card h3{left:8px;top:46px;font-size:8.5px;font-weight:600;color:var(--ink)}
.card p{left:8px;top:62px;width:82px;font-size:5.6px;line-height:12.5px;color:var(--body)}
.card svg{left:8px;top:14px}
.avatar{border-radius:50%;background:linear-gradient(160deg,#d9b79a,#7a5642)}
.signup label{font-size:7px;font-weight:700;color:var(--ink);left:17px}
.signup .field{font-size:5.6px;color:#8a8a8a;left:17px}
.signup .rule{left:17px;width:130px;height:1px;background:#9a9a9a}
</style>
</head>
<body>

<section class="page page-home">
  <div class="topbar">
    <div class="dot" style="left:47px;top:5px"></div>
    <span style="left:54px">LANGUAGES</span>
    <div class="dot" style="left:98px;top:5px"></div>
    <span style="left:105px">OUR SOCIAL</span>
    <div class="dot" style="left:418px;top:5px"></div>
    <div class="dot" style="left:428px;top:5px"></div>
    <div class="dot" style="left:438px;top:5px"></div>
    <div class="dot" style="left:448px;top:5px"></div>
  </div>

  <div class="hero photo" role="img" aria-label="Clay bowl of fresh tomato salsa with tortilla chips"></div>

  <div class="brand-mark" style="left:47px;top:28px"></div>
  <div class="brand-light" style="left:58px;top:24px">LA Brisa Roja</div>

  <nav class="nav" style="left:0;top:28px;width:498px;height:10px">
    <a style="left:214px">HOME</a>
    <a style="left:250px">ABOUT US</a>
    <a style="left:298px">PRODUCTS</a>
    <a style="left:348px">BLOG</a>
    <a style="left:384px">CONTACT US</a>
    <svg style="left:432px;top:0" width="7" height="7" viewBox="0 0 10 10"><circle cx="4" cy="4" r="3" fill="none" stroke="#fff" stroke-width="1.6"/><line x1="6.3" y1="6.3" x2="9.3" y2="9.3" stroke="#fff" stroke-width="1.8"/></svg>
    <svg style="left:446px;top:0" width="7" height="7" viewBox="0 0 10 10"><path d="M0 1h2l1.5 5h5l1-4H3" fill="none" stroke="#fff" stroke-width="1.4"/><circle cx="4" cy="8.5" r="1" fill="#fff"/><circle cx="8" cy="8.5" r="1" fill="#fff"/></svg>
  </nav>

  <div style="left:44px;top:68px;width:148px;height:148px">
    <div class="offer" style="left:0;top:0;width:148px;height:148px;background:var(--orange-soft)"></div>
    <div class="offer-title" style="top:24px">Salsa</div>
    <div class="offer-text" style="top:50px;left:12px;width:124px">Lorem ipsum dolor sit amet, consectetur adipiscing elit, sed do eiusmod</div>
    <div class="offer-pct" style="top:80px">50%</div>
    <div class="btn btn-light" style="left:44px;top:108px;width:60px;height:16px">SHOP NOW</div>
  </div>

  <h2 class="section-title" style="left:0;width:498px;text-align:center;top:280px">OUR PRODUCTS</h2>

  <div class="tile photo" style="left:46px;top:320px;background:linear-gradient(160deg,#e8e2da,#c0392b 60%,#5a3a22)" role="img" aria-label="White bowl of pico de gallo"><span class="tile-price">$ 30</span><span class="tile-name">LOREM IPSUM</span></div>
  <div class="tile photo" style="left:149px;top:320px;background:linear-gradient(160deg,#6a7a3a,#8a3a22 55%,#d9a84a)" role="img" aria-label="Salsa with tortilla chips"><span class="tile-price">$ 30</span><span class="tile-name">LOREM IPSUM</span></div>
  <div class="tile photo" style="left:252px;top:320px;background:linear-gradient(160deg,#4a4e4a,#b8352a 55%,#3a3a36)" role="img" aria-label="Dark bowl of salsa with peppers on slate"><span class="tile-price">$ 30</span><span class="tile-name">LOREM IPSUM</span></div>
  <div class="tile photo" style="left:355px;top:320px;background:linear-gradient(160deg,#c8372a,#d8533a 50%,#8a4a2a)" role="img" aria-label="Glass bowl of diced tomato salsa with cilantro"><span class="tile-price">$ 30</span><span class="tile-name">LOREM IPSUM</span></div>
  <div class="tile photo" style="left:46px;top:424px;background:linear-gradient(160deg,#b83a2a,#6a2a1a 55%,#d9a84a)" role="img" aria-label="Clay bowl of salsa with chips"><span class="tile-price">$ 30</span><span class="tile-name">LOREM IPSUM</span></div>
  <div class="tile photo" style="left:149px;top:424px;background:linear-gradient(160deg,#c0302a,#8a3a5a 50%,#4a4a48)" role="img" aria-label="Chopped tomato and onion salsa on grey stone"><span class="tile-price">$ 30</span><span class="tile-name">LOREM IPSUM</span></div>
  <div class="tile photo" style="left:252px;top:424px;background:linear-gradient(160deg,#d8a84a,#b84a2a 55%,#7a5a3a)" role="img" aria-label="Wooden bowl of salsa with chips"><span class="tile-price">$ 30</span><span class="tile-name">LOREM IPSUM</span></div>
  <div class="tile photo" style="left:355px;top:424px;background:linear-gradient(160deg,#4a3a36,#c0322a 55%,#8a2a22)" role="img" aria-label="Glass bowl of tomato salsa"><span class="tile-price">$ 30</span><span class="tile-name">LOREM IPSUM</span></div>

  <div class="photo" style="left:47px;top:558px;width:218px;height:171px;background:linear-gradient(150deg,#c9c3c6,#c4482a 50%,#e2d6cf)" role="img" aria-label="Glass jar of red salsa with chili peppers and lime"></div>
  <h2 class="section-title" style="left:279px;width:182px;text-align:center;top:578px">ABOUT US</h2>
  <p class="para center" style="left:284px;top:604px;width:172px">Lorem ipsum dolor sit amet, consectetur adipiscing elit, sed do eiusmod tempor incididunt ut labore et dolore magna aliqua. Ut enim ad minim veniam, quis nostrud exercitation ullamco laboris nisi ut aliquip ex ea commodo consequat. Duis aute irure dolor in reprehenderit in voluptate velit esse cillum dolore eu fugiat nulla pariatur.</p>
  <div class="btn" style="left:342px;top:691px;width:59px;height:16px">LEARN MORE</div>

  <h2 class="section-title" style="left:47px;top:773px">NATURAL INGREDIENTS</h2>
  <p class="para" style="left:47px;top:794px;width:160px">Lorem ipsum dolor sit amet, consectetur adipiscing elit, sed do eiusmod tempor incididunt ut labore et dolore magna aliqua.</p>
  <ul class="ingredients" style="left:47px;top:828px;width:150px;height:120px">
    <li style="left:0;top:0">Manzano Peppers</li>
    <li style="left:0;top:16px">Habanero Peppers</li>
    <li style="left:0;top:31px">Tomatillo</li>
    <li style="left:0;top:47px">Gralic/Ajo</li>
    <li style="left:0;top:63px">Cornstarch</li>
    <li class="two-line" style="left:0;top:75px;width:55px">Refrigerate After Opening</li>
    <li style="left:0;top:105px">Made</li>
    <li style="left:66px;top:0">Chile de Manzano</li>
    <li style="left:66px;top:16px">Chile de Habanero</li>
    <li style="left:66px;top:31px">salt /sal</li>
    <li style="left:66px;top:47px">Water/Agua</li>
    <li style="left:66px;top:63px">Fecula de Maiz</li>
    <li class="two-line" style="left:66px;top:75px;width:58px">Refrigerar Despues de abrir</li>
    <li style="left:66px;top:105px;width:80px">Hecho en Valle Rojo</li>
  </ul>
  <div class="btn" style="left:47px;top:952px;width:58px;height:16px">SHOP NOW</div>
  <div class="photo" style="left:234px;top:765px;width:218px;height:212px;background:linear-gradient(160deg,#d8d8d4,#c8342a 55%,#e6e4e0)" role="img" aria-label="Glass bowl of fresh pico de gallo with lime and tomato"></div>

  <footer class="footer" role="img" aria-label="Dark blurred salsa and chips background">
    <div class="dot" style="left:84px;top:56px;background:#fff"></div>
    <div class="dot" style="left:97px;top:56px;background:#fff"></div>
    <div class="dot" style="left:110px;top:56px;background:#fff"></div>
    <div class="dot" style="left:123px;top:56px;background:#fff"></div>
    <p class="footer-text center" style="left:40px;top:66px;width:130px">Lorem ipsum dolor sit amet, consectetur adipiscing elit, sed do eiusmod</p>
    <div class="brand-light" style="left:196px;top:38px;width:130px;text-align:center;font-size:13px">LA Brisa Roja</div>
    <p class="footer-text center" style="left:196px;top:63px;width:130px;font-weight:700">208-555-0142</p>
    <p class="footer-text center" style="left:196px;top:78px;width:130px;font-weight:700">hola@labrisaroja.com</p>
    <div class="footer-nav" style="left:363px;top:20px;width:80px;height:80px">
      <span style="top:0">HOME</span>
      <span style="top:14px">ABOUT US</span>
      <span style="top:28px">PRODUCTS</span>
      <span style="top:42px">BLOG</span>
      <span style="top:56px">CONTACT US</span>
    </div>
    <div style="left:47px;top:98px;width:404px;height:1px;background:rgba(255,255,255,.15)"></div>
    <p class="footer-text center" style="left:0;top:108px;width:498px">©Copyrights 2021 &nbsp;LA Brisa Roja &nbsp; | &nbsp; All Rights Reserved</p>
  </footer>
</section>

<section class="page page-app">
  <div class="brand-mark" style="left:46px;top:11px"></div>
  <div class="brand-dark" style="left:57px;top:7px">LA Brisa Roja</div>
  <nav class="nav-dark" style="left:0;top:12px;width:498px;height:10px">
    <span style="left:242px">HOME</span>
    <span style="left:278px">ABOUT US</span>
    <span style="left:326px">PRODUCTS</span>
    <span style="left:376px">BLOG</span>
    <span style="left:411px">CONTACT US</span>
  </nav>

  <h1 class="serif" style="left:47px;top:68px;font-size:23px;line-height:1;color:var(--ink);font-weight:400">LA Brisa Roja</h1>
  <p class="para" style="left:47px;top:106px;width:180px">Lorem ipsum dolor sit amet, consectetur adipiscing elit, sed do eiusmod tempor incididunt ut labore et dolore magna aliqua. Quis ipsum suspendisse ultrices gravida.</p>
  <div class="search">
    <span style="left:12px;top:7px;font-size:5.6px;color:#555">Search...</span>
    <div class="btn" style="left:126px;top:3px;width:35px;height:16px;font-family:'Archivo Narrow',sans-serif">GO</div>
  </div>
  <div class="store" style="left:47px;top:208px" role="img" aria-label="Mobile store download badge"></div>
  <div class="store" style="left:134px;top:208px" role="img" aria-label="Mobile store download badge"></div>

  <div class="photo" style="left:340px;top:29px;width:89px;height:61px;background:linear-gradient(160deg,#c8c6be,#c0392b 55%,#6a7a4a)" role="img" aria-label="Bowl of salsa"></div>
  <div class="photo" style="left:435px;top:29px;width:63px;height:34px;background:linear-gradient(160deg,#c8342a,#7a8a8a)" role="img" aria-label="Salsa close-up"></div>
  <div class="photo" style="left:290px;top:96px;width:140px;height:87px;background:linear-gradient(160deg,#6a8a3a,#c0342a 50%,#5a3a36)" role="img" aria-label="Glass bowl of salsa with lime and red pepper"></div>
  <svg style="left:352px;top:131px" width="16" height="16" viewBox="0 0 16 16"><circle cx="8" cy="8" r="8" fill="#dd6413"/><path d="M6.3 5v6l5-3z" fill="#fff"/></svg>
  <div class="photo" style="left:435px;top:69px;width:63px;height:90px;background:linear-gradient(160deg,#d9a84a,#c84a2a 60%,#b8843a)" role="img" aria-label="Salsa with tortilla chips"></div>
  <div class="photo" style="left:273px;top:190px;width:60px;height:60px;background:linear-gradient(160deg,#5a7a3a,#c8423a 55%,#d8d4cc)" role="img" aria-label="Bowl of pico de gallo"></div>
  <div class="photo" style="left:340px;top:190px;width:89px;height:87px;background:linear-gradient(160deg,#d9a84a,#9a3a22 55%,#4a3a2a)" role="img" aria-label="Dark bowl of salsa with chips"></div>
  <div class="photo" style="left:435px;top:164px;width:63px;height:125px;background:linear-gradient(160deg,#8aa04a,#c0342a 50%,#7a1a16)" role="img" aria-label="Salsa with lime"></div>

  <h2 class="section-title" style="left:0;width:498px;text-align:center;top:324px">Let's shop with us</h2>

  <div class="card" style="left:93px;top:375px">
    <svg width="28" height="22" viewBox="0 0 28 22" fill="none" stroke="#dd6413" stroke-width="1.3"><path d="M2 11h24a12 9 0 0 1-24 0z"/><path d="M6 10c1-5 5-7 8-6s6-2 8 6"/><line x1="9" y1="20" x2="19" y2="20"/></svg>
    <h3>Lorem Ipsum</h3>
    <p>Lorem ipsum dolor sit amet, consectetur adipiscing elit, sed do eiusmod tempor</p>
  </div>
  <div class="card" style="left:203px;top:375px">
    <svg width="28" height="22" viewBox="0 0 28 22" fill="none" stroke="#dd6413" stroke-width="1.3"><rect x="2" y="3" width="15" height="12" rx="1"/><path d="M17 7h5l4 4v4h-9"/><circle cx="7" cy="17" r="2.5"/><circle cx="21" cy="17" r="2.5"/></svg>
    <h3>Lorem Ipsum</h3>
    <p>Lorem ipsum dolor sit amet, consectetur adipiscing elit, sed do eiusmod tempor</p>
    <div style="left:16px;bottom:0;width:60px;height:2px;background:var(--orange)"></div>
  </div>
  <div class="card" style="left:313px;top:375px">
    <svg width="28" height="22" viewBox="0 0 28 22" fill="none" stroke="#dd6413" stroke-width="1.3"><path d="M3 12h20a10 8 0 0 1-20 0z"/><circle cx="9" cy="7" r="2.5"/><circle cx="15" cy="5" r="2.5"/><circle cx="19" cy="9" r="2"/></svg>
    <h3>Lorem Ipsum</h3>
    <p>Lorem ipsum dolor sit amet, consectetur adipiscing elit, sed do eiusmod tempor</p>
  </div>

  <div class="photo" style="left:0;top:522px;width:498px;height:166px;background:radial-gradient(ellipse at 75% 50%,#8a2a22 0%,#3a3a3a 45%,#2c2c2c 100%)" role="img" aria-label="Bowl of salsa with peppers, onion and lime on dark slate"></div>
  <div style="left:47px;top:530px;width:146px;height:146px">
    <div class="offer" style="left:0;top:0;width:146px;height:146px;background:var(--orange)"></div>
    <div class="offer-title" style="top:23px">Salsa</div>
    <div class="offer-text" style="top:49px;left:12px;width:122px">Lorem ipsum dolor sit amet, consectetur adipiscing elit, sed do eiusmod</div>
    <div class="offer-pct" style="top:79px">50%</div>
    <div class="btn btn-light" style="left:43px;top:107px;width:60px;height:16px">SHOP NOW</div>
  </div>

  <h2 class="section-title" style="left:0;width:488px;text-align:center;top:722px">Testimonial</h2>
  <div class="serif" style="left:220px;top:735px;font-size:60px;line-height:1;color:#f5c9ad">“</div>
  <span style="left:63px;top:760px;font-size:8px;color:var(--ink)">‹</span>
  <span style="left:409px;top:760px;font-size:8px;color:var(--ink)">›</span>
  <p class="center" style="left:80px;top:755px;width:320px;font-size:5.6px;line-height:10px;color:var(--ink)">Lorem ipsum dolor sit amet, consectetur adipiscing elit, sed do eiusmod tempor incididunt ut labore et dolore magna aliqua. Quis ipsum suspendisse ultrices gravida. Risus commodo viverra maecenas accumsan lacus vel facilisis.</p>
  <div class="avatar" style="left:206px;top:793px;width:18px;height:18px" role="img" aria-label="Customer portrait"></div>
  <div class="avatar" style="left:230px;top:791px;width:22px;height:22px" role="img" aria-label="Customer portrait"></div>
  <div class="avatar" style="left:258px;top:793px;width:18px;height:18px" role="img" aria-label="Customer portrait"></div>
  <p style="left:0;width:482px;text-align:center;top:818px;font-size:6px;font-weight:700;color:var(--ink)">Marisol Venn</p>

  <div style="left:0;top:862px;width:498px;height:316px;background:var(--orange)"></div>
  <h2 class="serif" style="left:0;width:498px;text-align:center;top:881px;font-size:14px;line-height:1;color:var(--white);font-weight:400">Online Food World</h2>
  <div class="photo" style="left:79px;top:917px;width:167px;height:221px;background:radial-gradient(ellipse at 60% 50%,#b8342a 0%,#8a4a26 45%,#2a1e16 100%)" role="img" aria-label="Clay bowl of fresh salsa with tortilla chips"></div>
  <div class="signup" style="left:253px;top:917px;width:166px;height:221px;background:var(--white)">
    <h3 class="serif" style="left:0;width:166px;text-align:center;top:21px;font-size:10px;font-weight:400;color:var(--ink)">Sign up</h3>
    <label style="top:51px">Name</label>
    <span class="field" style="top:65px">Lorem Ipsum</span>
    <div class="rule" style="top:80px"></div>
    <label style="top:93px">Email</label>
    <span class="field" style="top:107px">email@example.com</span>
    <div class="rule" style="top:122px"></div>
    <label style="top:135px">Password</label>
    <span class="field" style="top:148px">..........</span>
    <div class="rule" style="top:164px"></div>
    <div class="btn" style="left:59px;top:182px;width:48px;height:16px;font-family:'Archivo Narrow',sans-serif;font-weight:700">Sign up</div>
  </div>
  <p style="left:0;width:498px;text-align:center;top:1153px;font-size:5.6px;color:var(--white)">©Copyrights 2021 Company Name &nbsp;| &nbsp; All Rights Reserved</p>
</section>

</body>
</html>
```